Flyer-Design für Home Staging und Home Design
Zielgruppe
Raumwerk-17: Home Staging und Home Design
Kontaktdaten:
Raumwerk 17
Marlene Haupt Str. 46 c
04109 Leipzig
Tel.: 0176-3918457
info@raumwerk-17.example
www.raumwerk-17.example
Aufgabenstellung
- elegant / modern
- anbei ein Beispiel meiner anderen Firma (als kleine Orientierung) - 1. Anhang

```html
<!DOCTYPE html>
<html lang="de">
<head>
<meta charset="utf-8">
<title>Raumwerk 17 – Flyer Home Staging &amp; Home Design</title>
<link href="https://fonts.googleapis.com/css2?family=Didact+Gothic&display=swap" rel="stylesheet">
<style>
  :root {
    --stage: #333333;
    --paper: #ffffff;
    --ink: #1a1a1a;
    --gold: #d6a52a;
    --bronze: #7b5432;
  }
  * { margin: 0; padding: 0; box-sizing: border-box; }
  html, body { width: 1200px; height: 675px; overflow: hidden; background: var(--stage); }
  body { position: relative; font-family: "Didact Gothic", "Helvetica Neue", Arial, sans-serif; color: var(--ink); }

  .flyer { position: absolute; top: 141px; width: 558px; height: 394px; background: var(--paper); overflow: hidden; }
  .flyer--front { left: 31px; }
  .flyer--back { left: 611px; }
  .flyer svg { position: absolute; inset: 0; width: 100%; height: 100%; }

  .front__tagline {
    position: absolute; top: 12px; left: 0; width: 100%;
    text-align: center; font-size: 29px; letter-spacing: 0.2px; font-weight: 400;
  }
  .brand-name {
    position: absolute; font-weight: 400; color: var(--ink); white-space: nowrap;
  }
  .front__brand { top: 62px; left: 0; width: 100%; text-align: center; font-size: 50px; }
  .back__brand { top: 56px; left: 150px; width: 250px; text-align: center; font-size: 44px; }

  .back__contact {
    position: absolute; left: 57px; top: 215px;
    font-size: 17px; line-height: 22px; font-style: normal;
  }
</style>
</head>
<body>

<section class="flyer flyer--front" aria-label="Flyer Vorderseite">
  <svg viewBox="0 0 558 394" preserveAspectRatio="none">
    <defs>
      <linearGradient id="goldBand" x1="0" y1="0" x2="1" y2="1">
        <stop offset="0" stop-color="var(--gold)"/>
        <stop offset="1" stop-color="var(--bronze)"/>
      </linearGradient>
      <linearGradient id="kitchenTone" x1="0" y1="0" x2="0" y2="1">
        <stop offset="0.35" stop-color="#ffffff"/>
        <stop offset="0.7" stop-color="#e8ddd0"/>
        <stop offset="1" stop-color="#cfc3b4"/>
      </linearGradient>
      <linearGradient id="sketchTone" x1="0" y1="0" x2="0" y2="1">
        <stop offset="0" stop-color="#f1f1f1"/>
        <stop offset="1" stop-color="#dcdcdc"/>
      </linearGradient>
      <linearGradient id="bathTone" x1="0" y1="0" x2="0" y2="1">
        <stop offset="0" stop-color="#d8d2cb"/>
        <stop offset="1" stop-color="#b9ada0"/>
      </linearGradient>
      <linearGradient id="livingTone" x1="0" y1="0" x2="0" y2="1">
        <stop offset="0" stop-color="#e6e2dc"/>
        <stop offset="0.6" stop-color="#a89a8a"/>
        <stop offset="1" stop-color="#6e655c"/>
      </linearGradient>
    </defs>
    <polygon role="img" aria-label="Innenraum-Skizze eines Arbeitszimmers" points="0,0 37.5,0 112,166 0,197" fill="url(#sketchTone)"/>
    <polygon role="img" aria-label="Badezimmer mit freistehender Wanne" points="0,197 112,166 225,394 0,394" fill="url(#bathTone)"/>
    <polygon role="img" aria-label="Offene Küche, halb Skizze, halb Fotografie" points="37.5,0 525,0 375,394 225,394" fill="url(#kitchenTone)"/>
    <polygon role="img" aria-label="Skizze eines Essbereichs" points="525,0 558,0 558,153 462,181" fill="url(#sketchTone)"/>
    <polygon role="img" aria-label="Wohn- und Schlafbereich mit Kronleuchter" points="462,181 558,153 558,394 375,394" fill="url(#livingTone)"/>
    <line x1="37.5" y1="0" x2="225" y2="394" stroke="url(#goldBand)" stroke-width="5"/>
    <line x1="525" y1="0" x2="375" y2="394" stroke="url(#goldBand)" stroke-width="5"/>
    <line x1="0" y1="197" x2="112" y2="166" stroke="url(#goldBand)" stroke-width="5"/>
    <line x1="462" y1="181" x2="558" y2="153" stroke="url(#goldBand)" stroke-width="5"/>
  </svg>
  <h1 class="front__tagline">HOME STAGING &amp; HOME DESIGN</h1>
  <p class="brand-name front__brand">Raumwerk 17</p>
</section>

<section class="flyer flyer--back" aria-label="Flyer Rückseite">
  <svg viewBox="0 0 558 394" preserveAspectRatio="none">
    <defs>
      <linearGradient id="barH" x1="0" y1="0" x2="1" y2="0">
        <stop offset="0" stop-color="var(--gold)"/>
        <stop offset="1" stop-color="var(--bronze)"/>
      </linearGradient>
      <linearGradient id="barV" x1="0" y1="0" x2="0" y2="1">
        <stop offset="0" stop-color="var(--bronze)"/>
        <stop offset="1" stop-color="var(--gold)"/>
      </linearGradient>
      <linearGradient id="roomWash" x1="0" y1="0" x2="1" y2="0">
        <stop offset="0" stop-color="#ffffff"/>
        <stop offset="0.35" stop-color="#eeeeec"/>
        <stop offset="1" stop-color="#cfcac3"/>
      </linearGradient>
    </defs>
    <rect role="img" aria-label="Aquarell-Skizze eines Wohnzimmers mit Sofa und Kronleuchter" x="182" y="0" width="376" height="394" fill="url(#roomWash)"/>
    <rect x="0" y="19" width="558" height="12" fill="url(#barH)"/>
    <rect x="0" y="359" width="558" height="12" fill="url(#barH)"/>
    <rect x="26" y="0" width="16" height="394" fill="url(#barV)"/>
    <rect x="526" y="0" width="13" height="394" fill="url(#barV)"/>
  </svg>
  <p class="brand-name back__brand">Raumwerk 17</p>
  <address class="back__contact">
    Raumwerk 17<br>
    Marlene Haupt Str. 46 c<br>
    04109 Leipzig<br>
    Tel.: 0176-3918457<br>
    info@raumwerk-17.example<br>
    www.raumwerk-17.example
  </address>
</section>

</body>
</html>
```